Croatia Luxury Cruise Brochure

1) Front page instead of By Orchard Path with Liesl please put by Pinecrest Harbor Guild – same on the last page where you have her contacts
2) Can you please add into the second page where you have ‘Welcome to your Croatia trip’ itinerary at glance. You can put it just below the text you have. Create a nice looking table .
D1 August 05, 2023 Arrival to Dubrovnik , Welcome cocktail party on Dubrovnik city walls
D2 August 06, 2023 Dubrovnik Highlights city tour – Embark sail to Elafiti
D3 August 07, 2023 Sail to Mljet island and day at leisure at sea
D4 August 08, 2023 Peljesac Wine Tasting with Live Music – Sail to Korcula
D5 August 09, 2023 Korcula Highlights Explorer Tour & Local Estate Dinner
D6 August 10, 2023 Korcula to Vis Island sail
D7 August 11, 2023 Vis Militarty Tour -sail to Pakleni Islands Bortelli sunset cocktails
D8 August 12, 2023 Hvar island – sail to Split
D9 August 13, 2023 Disembark – Split & Trogir ORVALD tours with 6-course wine dinner
D10 August 14, 2023 Fly out
Note: All tours & Experiences are optional add ons except the Cocktail reception on Dubrovnik city walls
3) Changes to the itinerary:
D1 is now arrival to Dubrovnik day earlier (AUGU5) and the rest is all moved accordingly. Please check the link
https://portal.kelvoro-desk. com/itinerary/custom-trip-prepared-for-liesl-group/
4) Inclusion/Exclusion page we need to update a little. Please make 3 different categories with a note for booking conditions.
Inclusions
• All transfers per itinerary including airport pick up and drop off
• 7 nights cruise on MS Dovetail on half board basis
• All meals stated per itinerary
• Captains dinner
• Unlimited water
• Masseuse on board
• Service of 11 crew members
• Cruise director
• Unlimited WiFi
• Daily cleaning
• Arrival refreshments
• Premium docking
• Usage of non motorized water toys
• Exclusive cocktail reception on Dubrovnik city walls with live music and snacks
Optional Tours
• Dubrovnik Highlights Explorer tour
• Peljesac Wine tour with live music
• Korcula explorer tour with local estate dinner
• Vis Military tour
• Bortelli Lounge bar reservation (min spend EUR100 per person)
• Split & Trogir ORVALD Explorer tour
• 6-course farewell dinner with local wine pairing
• 1 night post stay in Velmont 5* hotel in Split (This is added on optional)
Extras
• Tips for the crew
• Beverage consumption
• Usage of motorized water toys – EUR150 per hour
• International flights
• Any personal expenses
Booking conditions
30 % non-refundable deposit needed upon confirmation
Balance of the trip and any optional tours picked are due 06 May, 2023
Luxury travelers from USA and Canada
Tourism

```html
<!DOCTYPE html>
<html lang="en">
<head>
<meta charset="utf-8">
<title>Croatia – Luxury Explorer Cruise Brochure</title>
<link rel="stylesheet" href="https://fonts.googleapis.com/css2?family=Libre+Caslon+Text:wght@400;700&family=Figtree:wght@400;500;600&family=IBM+Plex+Mono:wght@400;500&display=swap">
<style>
  :root {
    --canvas: #c8c8c8;
    --coral: #e1533f;
    --ink: #1f2a33;
    --paper: #ffffff;
    --sea-deep: #0d3f78;
    --sea-mid: #1f6fb4;
    --sea-light: #3e9bd4;
    --sky-warm: #f2d7b8;
    --hill: #3d4a35;
    --white: #ffffff;
    --rule: rgba(255,255,255,.35);
  }
  * { box-sizing: border-box; margin: 0; padding: 0; }
  html, body { width: 1200px; height: 900px; overflow: hidden; }
  body {
    background: var(--canvas);
    font-family: "Figtree", sans-serif;
    color: var(--ink);
    position: relative;
  }

  /* ---------- Front cover ---------- */
  .cover {
    position: absolute;
    left: 50px; top: 205px;
    width: 340px; height: 480px;
    overflow: hidden;
    box-shadow: 0 8px 24px rgba(0,0,0,.18);
  }
  .cover__photo {
    position: absolute; inset: 0;
    background:
      radial-gradient(ellipse at 20% 55%, rgba(233,138,44,.85) 0%, rgba(233,138,44,0) 38%),
      linear-gradient(180deg, #e9e4e0 0%, var(--sky-warm) 28%, #c9b7a6 42%, #8f8478 55%, #4f5a60 72%, #2a3a48 100%);
  }
  .cover__title {
    position: absolute;
    top: 48px; right: 34px;
    text-align: right;
  }
  .cover__name {
    font-family: "Libre Caslon Text", serif;
    font-size: 62px; line-height: 1;
    color: var(--coral);
    font-weight: 400;
  }
  .cover__tagline {
    font-size: 10.5px; font-weight: 500;
    color: var(--ink);
    margin-top: 4px;
  }
  .cover__credit {
    font-size: 10.5px; font-weight: 600;
    color: var(--ink);
    margin-top: 3px;
  }
  .dates {
    position: absolute;
    right: 22px; bottom: 22px;
    width: 190px;
  }
  .dates__label {
    background: var(--coral);
    color: var(--white);
    font-size: 10px; font-weight: 600;
    letter-spacing: .04em;
    text-transform: uppercase;
    padding: 7px 12px 6px;
    border-radius: 10px 10px 0 0;
  }
  .dates__list {
    background: var(--paper);
    list-style: none;
    padding: 4px 12px 6px;
    font-family: "IBM Plex Mono", monospace;
    font-size: 9.5px;
  }
  .dates__list li { padding: 5px 0; }

  /* ---------- Opening spread ---------- */
  .spread {
    position: absolute;
    left: 420px; top: 205px;
    width: 740px; height: 480px;
    overflow: hidden;
    box-shadow: 0 8px 24px rgba(0,0,0,.18);
  }
  .spread__photo {
    position: absolute; inset: 0;
    background:
      linear-gradient(170deg, #dfe3ec 0%, #b9c3cf 10%, var(--hill) 22%, #55603f 34%, var(--sea-light) 46%, var(--sea-mid) 62%, var(--sea-deep) 100%);
  }
  .spread__gutter {
    position: absolute;
    top: 0; bottom: 0; left: 350px; width: 40px;
    background: linear-gradient(90deg, rgba(0,0,0,0) 0%, rgba(0,0,0,.28) 50%, rgba(255,255,255,.08) 55%, rgba(0,0,0,0) 100%);
  }
  .intro {
    position: absolute;
    left: 408px; top: 34px;
    width: 310px;
    color: var(--white);
  }
  .intro__heading {
    font-family: "Libre Caslon Text", serif;
    font-weight: 700;
    font-size: 17px; line-height: 1.25;
    margin-bottom: 9px;
  }
  .intro__body {
    font-size: 8px; line-height: 1.45;
    margin-bottom: 6px;
  }

  /* ---------- Itinerary at a glance ---------- */
  .itinerary { margin-top: 10px; }
  .itinerary__title {
    font-family: "Libre Caslon Text", serif;
    font-weight: 700;
    font-size: 11px;
    margin-bottom: 4px;
  }
  .itinerary__table {
    width: 100%;
    border-collapse: collapse;
    font-size: 7.5px; line-height: 1.3;
  }
  .itinerary__table th {
    background: var(--coral);
    color: var(--white);
    font-weight: 600;
    text-transform: uppercase;
    letter-spacing: .04em;
    text-align: left;
    padding: 3px 5px;
  }
  .itinerary__table td {
    padding: 2.5px 5px;
    border-bottom: 1px solid var(--rule);
    vertical-align: top;
  }
  .itinerary__day { width: 26px; font-weight: 600; }
  .itinerary__date { width: 44px; font-family: "IBM Plex Mono", monospace; white-space: nowrap; }
  .itinerary__note {
    font-size: 7px; font-style: normal;
    margin-top: 5px; opacity: .9;
  }
</style>
</head>
<body>

  <section class="cover" aria-label="Front cover">
    <div class="cover__photo" role="img" aria-label="Photograph of a white mini cruiser at sea near a wooded island at sunset"></div>
    <header class="cover__title">
      <h1 class="cover__name">Croatia</h1>
      <p class="cover__tagline">Luxury explorer cruise on Dovetail mini cruiser</p>
      <p class="cover__credit">by Pinecrest Harbor Guild</p>
    </header>
    <div class="dates">
      <div class="dates__label">Travel dates</div>
      <ul class="dates__list">
        <li>05 August - 14 August, 2023</li>
      </ul>
    </div>
  </section>

  <section class="spread" aria-label="Opening spread">
    <div class="spread__photo" role="img" aria-label="Aerial photograph of a mini cruiser sailing in blue water past a green island town"></div>
    <div class="spread__gutter"></div>
    <article class="intro">
      <h2 class="intro__heading">The Croatian Coast is the premiere setting for the ultimate island hopping experience.</h2>
      <p class="intro__body">The Dalmatian Islands in Croatia are among the most famous in the Mediterranean region. Wild, rugged, and hiding a thousand-year history, many are protected as national park and offer a varied and diverse cruising ground for an yacht charter. The cruising is splendid encompassing long and short passages to charming anchorages amid rocky islets, ancient villages steeped in history, and translucent waters.</p>
      <p class="intro__body">In total Croatia has over 1200 islands and islets to explore and visit so depending on your travel preference and travel style the combinations of itineraries are endless. Enjoy your cruise on mini cruiser Dovetail by visiting highlights of Adriatic coastline.</p>

      <section class="itinerary">
        <h3 class="itinerary__title">Itinerary at a glance</h3>
        <table class="itinerary__table">
          <thead>
            <tr><th>Day</th><th>Date</th><th>Programme</th></tr>
          </thead>
          <tbody>
            <tr><td class="itinerary__day">D1</td><td class="itinerary__date">Aug 05</td><td>Arrival to Dubrovnik, welcome cocktail party on Dubrovnik city walls</td></tr>
            <tr><td class="itinerary__day">D2</td><td class="itinerary__date">Aug 06</td><td>Dubrovnik Highlights city tour – embark, sail to Elafiti</td></tr>
            <tr><td class="itinerary__day">D3</td><td class="itinerary__date">Aug 07</td><td>Sail to Mljet island and day at leisure at sea</td></tr>
            <tr><td class="itinerary__day">D4</td><td class="itinerary__date">Aug 08</td><td>Peljesac Wine Tasting with Live Music – sail to Korcula</td></tr>
            <tr><td class="itinerary__day">D5</td><td class="itinerary__date">Aug 09</td><td>Korcula Highlights Explorer Tour &amp; Local Estate Dinner</td></tr>
            <tr><td class="itinerary__day">D6</td><td class="itinerary__date">Aug 10</td><td>Korcula to Vis Island sail</td></tr>
            <tr><td class="itinerary__day">D7</td><td class="itinerary__date">Aug 11</td><td>Vis Military Tour – sail to Pakleni Islands, Bortelli sunset cocktails</td></tr>
            <tr><td class="itinerary__day">D8</td><td class="itinerary__date">Aug 12</td><td>Hvar island – sail to Split</td></tr>
            <tr><td class="itinerary__day">D9</td><td class="itinerary__date">Aug 13</td><td>Disembark – Split &amp; Trogir ORVALD tours with 6-course wine dinner</td></tr>
            <tr><td class="itinerary__day">D10</td><td class="itinerary__date">Aug 14</td><td>Fly out</td></tr>
          </tbody>
        </table>
        <p class="itinerary__note">Note: All tours &amp; experiences are optional add-ons except the cocktail reception on Dubrovnik city walls.</p>
      </section>
    </article>
  </section>

</body>
</html>
```